The Kestrel Partners Business Cards

We need a sleek looking business card for our real estate company. Looking for a clean, modern, eye catching design on a standard size business card.

No more submissions please! Thank you!

Target Market(s)

General Public/Real Estate Clients

Industry/Entity Type

Real Estate

Contact Information for Business Card

Cards will be customized for each agent.

Colors

Designer to choose only greyscale colors for use in the design.

Requirements
Must have
• Black, white, gray color pallet, Photo area for headshot on the front of the card

```html
<!DOCTYPE html>
<html lang="en">
<head>
<meta charset="utf-8">
<title>The Kestrel Partners – Business Cards</title>
<link href="https://fonts.googleapis.com/css2?family=Montserrat:wght@300;400;500;700&display=swap" rel="stylesheet">
<style>
  :root {
    --stage: #2c2c2e;
    --card: #1e2433;
    --card-deep: #181d29;
    --ink: #ffffff;
    --ink-soft: #d6d8de;
    --photo: #f4f4f5;
    --ring: #b9b4b4;
  }
  * { margin: 0; padding: 0; box-sizing: border-box; }
  html, body { width: 1200px; height: 976px; overflow: hidden; }
  body {
    background: var(--stage);
    font-family: "Montserrat", sans-serif;
    color: var(--ink);
    position: relative;
  }
  .card {
    position: absolute;
    width: 560px;
    height: 320px;
    background: linear-gradient(160deg, var(--card) 0%, var(--card-deep) 100%);
    overflow: hidden;
    box-shadow: 0 14px 30px rgba(0,0,0,.45);
  }
  .card--back { left: 600px; top: 110px; }
  .card--front { left: 40px; top: 520px; }

  /* back */
  .back-brand {
    position: absolute; inset: 0;
    display: flex; align-items: center; justify-content: center; gap: 14px;
  }
  .brand-mark { width: 14px; height: 14px; background: var(--ink); }
  .brand-name {
    font-weight: 500; font-size: 30px; letter-spacing: 3px; text-transform: uppercase;
    color: var(--ink);
  }

  /* front */
  .photo { position: absolute; inset: 0; }
  .agent { position: absolute; left: 150px; top: 26px; }
  .agent-name { font-size: 19px; letter-spacing: .5px; text-transform: uppercase; line-height: 1; }
  .agent-name .first { font-weight: 300; }
  .agent-name .last { font-weight: 700; }
  .agent-role { font-size: 9px; font-weight: 400; margin-top: 6px; color: var(--ink-soft); }
  .agent-rule { width: 26px; height: 3px; background: var(--ink); margin-top: 8px; }

  .contacts { position: absolute; left: 150px; top: 100px; list-style: none; }
  .contacts li {
    display: flex; align-items: center; gap: 10px;
    font-size: 11px; font-weight: 400; height: 20px; color: var(--ink);
  }
  .contacts svg { width: 11px; height: 11px; fill: var(--ink); flex: none; }

  .front-brand {
    position: absolute; left: 26px; top: 226px;
    display: flex; align-items: center; gap: 9px;
  }
  .front-brand .brand-mark { width: 8px; height: 8px; }
  .front-brand .brand-name { font-size: 14px; letter-spacing: 1.5px; }

  .address {
    position: absolute; right: 268px; bottom: 20px; text-align: right;
    font-size: 11px; line-height: 1.45; font-weight: 400;
  }
</style>
</head>
<body>

  <section class="card card--back" aria-label="Card back">
    <div class="back-brand">
      <span class="brand-mark"></span>
      <span class="brand-name">The Kestrel Partners</span>
    </div>
  </section>

  <section class="card card--front" aria-label="Card front">
    <svg class="photo" viewBox="0 0 560 320" width="560" height="320">
      <circle cx="640" cy="150" r="318" fill="none" stroke="var(--ring)" stroke-width="5"/>
      <circle cx="640" cy="150" r="308" fill="var(--card-deep)"/>
      <circle cx="640" cy="150" r="302" fill="var(--photo)" role="img" aria-label="Agent headshot photo"/>
    </svg>

    <div class="agent">
      <p class="agent-name"><span class="first">Dana</span> <span class="last">Whitfield</span></p>
      <p class="agent-role">Realtor / Broker</p>
      <div class="agent-rule"></div>
    </div>

    <ul class="contacts">
      <li><svg viewBox="0 0 24 24"><path d="M6.6 10.8a15 15 0 0 0 6.6 6.6l2.2-2.2c.3-.3.7-.4 1-.2 1.1.4 2.3.6 3.6.6.6 0 1 .4 1 1V20c0 .6-.4 1-1 1C10.6 21 3 13.4 3 4c0-.6.4-1 1-1h3.5c.6 0 1 .4 1 1 0 1.3.2 2.5.6 3.6.1.3 0 .7-.2 1z"/></svg>555.014.2290</li>
      <li><svg viewBox="0 0 24 24"><path d="M3 8h3V3h10l3 3v2h2v12H3zM8 5v3h9V6.8L15.2 5zM6 12v2h3v-2zm5 0v2h3v-2zm5 0v2h3v-2zM6 16v2h3v-2zm5 0v2h3v-2zm5 0v2h3v-2z"/></svg>555.014.2291</li>
      <li><svg viewBox="0 0 24 24"><path d="M2 5h20v14H2zm2 2v.5l8 5 8-5V7z"/></svg>info@kestrelpartners.com</li>
      <li><svg viewBox="0 0 24 24"><path d="M12 2a10 10 0 1 0 0 20 10 10 0 0 0 0-20zm6.9 9h-3a15 15 0 0 0-1.3-6A8 8 0 0 1 18.9 11zM12 4c.9 1.3 1.7 3.8 1.9 7h-3.8C10.3 7.8 11.1 5.3 12 4zM9.4 5a15 15 0 0 0-1.3 6h-3A8 8 0 0 1 9.4 5zM5.1 13h3a15 15 0 0 0 1.3 6A8 8 0 0 1 5.1 13zM12 20c-.9-1.3-1.7-3.8-1.9-7h3.8c-.2 3.2-1 5.7-1.9 7zm2.6-1a15 15 0 0 0 1.3-6h3a8 8 0 0 1-4.3 6z"/></svg>www.kestrelpartners.com</li>
    </ul>

    <div class="front-brand">
      <span class="brand-mark"></span>
      <span class="brand-name">The Kestrel Partners</span>
    </div>

    <address class="address" style="font-style:normal">
      58 Harrow Lane, Linden Court<br>
      Maple ST, Easton, FL- 30417
    </address>
  </section>

</body>
</html>
```